Window Advertisment for Rentals Company

I own a property rental company in Cyprus and I am looking for an eye catching design to place in my window to attract passers by.

Please check the attachment for more details.

Ad size to be 309cm x 204cm landscape

The font of the logo is velocity

Target Market(s)

Property Owners

Industry/Entity Type

It Company

Requirements
Must have
• The colours from my logo and be eye catching and make passers by take notice

```html
<!DOCTYPE html>
<html lang="en">
<head>
<meta charset="utf-8">
<title>Harbour Stays Cyprus – Window Advertisement</title>
<link rel="stylesheet" href="https://fonts.googleapis.com/css2?family=Righteous&family=Roboto+Condensed:wght@300;700&display=swap">
<style>
  :root {
    --frame: #0b0b0b;
    --sun-yellow: #fcc50f;
    --wave-orange: #f26f25;
    --wave-edge: #b8440f;
    --brown: #3f1708;
    --ink: #140b05;
    --white: #ffffff;
    --sea: #3fb7c4;
    --sand: #efe3d6;
    --sky: #b9d8ee;
    --grass: #5f8f3a;
  }
  * { margin: 0; padding: 0; box-sizing: border-box; }
  html, body {
    width: 1200px; height: 800px; overflow: hidden;
    background: var(--frame);
  }
  .poster {
    position: relative; width: 1200px; height: 800px;
    background: var(--frame); overflow: hidden;
  }
  .artwork { position: absolute; left: 0; top: 0; }
  .wave-text {
    font-family: "Righteous", sans-serif;
    font-size: 37px; fill: var(--white); letter-spacing: 1px;
  }
  .reach-tag {
    position: absolute; left: 24px; top: 16px; width: 650px; height: 52px;
    background: var(--sun-yellow); color: var(--ink);
    font-family: "Roboto Condensed", sans-serif; font-weight: 700;
    font-size: 29px; line-height: 52px; padding-left: 30px;
    letter-spacing: -0.2px;
  }
  .call-line {
    position: absolute; left: 718px; top: 310px;
    font-family: "Roboto Condensed", sans-serif; color: var(--ink);
    white-space: nowrap;
  }
  .call-line .label { font-weight: 300; font-size: 42px; letter-spacing: -1px; }
  .call-line .number { font-weight: 700; font-size: 68px; letter-spacing: -1px; margin-left: 6px; }
  .headline {
    position: absolute; left: 40px; top: 462px; width: 440px;
    text-align: right; font-family: "Righteous", sans-serif; font-weight: 400;
    font-size: 45px; line-height: 56px; color: var(--ink);
    letter-spacing: 0.5px; word-spacing: 6px; white-space: nowrap;
  }
  .brand-card {
    position: absolute; left: 526px; top: 508px; width: 312px; height: 180px;
    background: var(--white);
    box-shadow: -10px 0 0 #e39a1c;
    display: flex; align-items: center; justify-content: center; gap: 12px;
  }
  .brand-card .mark {
    width: 34px; height: 34px; border-radius: 50%; background: var(--wave-orange);
  }
  .brand-card .brand-name {
    font-family: "Righteous", sans-serif; font-size: 30px; line-height: 32px;
    color: var(--wave-orange);
  }
  .benefits { position: absolute; left: 838px; top: 522px; list-style: none; }
  .benefits li {
    width: 310px; height: 45px; margin-bottom: 10px;
    background: var(--brown); color: var(--white);
    font-family: "Roboto Condensed", sans-serif; font-weight: 700;
    font-size: 30px; line-height: 45px; text-align: right; padding-right: 16px;
    letter-spacing: 0.5px;
  }
  .web-address {
    position: absolute; left: 608px; top: 698px; width: 534px; text-align: right;
    font-family: "Righteous", sans-serif; font-size: 31px; color: var(--brown);
    letter-spacing: 1.5px;
  }
</style>
</head>
<body>
<main class="poster">
  <svg class="artwork" width="1200" height="800" viewBox="0 0 1200 800">
    <defs>
      <linearGradient id="resortScene" x1="0" y1="0" x2="0" y2="1">
        <stop offset="0" stop-color="var(--sky)"/>
        <stop offset="0.18" stop-color="#d9d2c8"/>
        <stop offset="0.35" stop-color="#9a8d7c"/>
        <stop offset="0.5" stop-color="var(--grass)"/>
        <stop offset="0.6" stop-color="var(--sand)"/>
        <stop offset="0.8" stop-color="#e6d6c6"/>
        <stop offset="1" stop-color="var(--sea)"/>
      </linearGradient>
      <path id="waveLine" d="M84 394 C 250 356, 470 350, 830 448"/>
    </defs>
    <rect class="resort-photo" x="24" y="16" width="1156" height="440" fill="url(#resortScene)"
          role="img" aria-label="Photo of modern beachfront villas with palm trees, a sandy beach with families playing and clear turquoise sea"/>
    <path class="yellow-field" d="M24 440 C 300 410, 600 440, 880 478 C 1020 494, 1110 472, 1180 452 L1180 780 L24 780 Z" fill="var(--sun-yellow)"/>
    <path class="orange-wave" d="M24 376 C 150 350, 260 330, 380 336 C 560 346, 740 410, 900 418 C 1020 424, 1110 404, 1180 392 L1180 456 C 1110 476, 1020 494, 880 478 C 600 440, 300 410, 24 440 Z" fill="var(--wave-orange)"/>
    <path d="M24 440 C 300 410, 600 440, 880 478 C 1020 494, 1110 472, 1180 452" fill="none" stroke="var(--wave-edge)" stroke-width="3"/>
    <text class="wave-text"><textPath href="#waveLine" textLength="745" lengthAdjust="spacing">connect with over 35 leading websites</textPath></text>
  </svg>

  <div class="reach-tag">BE SEEN BY 100+ MILLION TRAVELLERS PER MONTH</div>

  <p class="call-line"><span class="label">Call us:</span><span class="number">23 555014</span></p>

  <h1 class="headline">We are looking<br>for villas and<br>apartments to<br>fulfill our growing<br>demand of rentals</h1>

  <div class="brand-card">
    <span class="mark"></span>
    <span class="brand-name">harbour stays<br>cyprus</span>
  </div>

  <ul class="benefits">
    <li>LOW COMMISSIONS</li>
    <li>QUICK PAYOUTS</li>
    <li>FREE ADVERTISING</li>
  </ul>

  <p class="web-address">www.harbourstayscyprus.com</p>
</main>
</body>
</html>
```